Corin Abbott Business Cards

We Need two Business Cards with bleeds. the only difference between the two cards is the backaround color one lilac and pink. Attached we have the cards please match up the logo's and text. Take out the orange box out.

Target Market(s)

double-sided business cards

Industry/Entity Type

Business

Logo Text

match up as best as possible

Colors
f59195
d2a4cc

Requirements
Must have
• n/a
Nice to have
• n/a
Should not have
• n/a

```html
<!DOCTYPE html>
<html lang="en">
<head>
<meta charset="utf-8">
<title>Corin Abbott Business Cards</title>
<link href="https://fonts.googleapis.com/css2?family=Arimo:ital,wght@0,400;0,700;1,700&display=swap" rel="stylesheet">
<style>
  :root {
    --page: #ffffff;
    --ink: #111111;
    --white: #ffffff;
    --lilac: #d2a4cc;
    --lilac-deep: #6e3362;
    --lilac-mark: #b57cb6;
    --lilac-accent: #7a3b70;
    --pink: #f59195;
    --pink-deep: #8f3a55;
    --pink-mark: #b55a72;
    --pink-accent: #8a3d55;
  }
  * { box-sizing: border-box; margin: 0; padding: 0; }
  html, body {
    width: 1200px; height: 900px; overflow: hidden;
    background: var(--page);
    font-family: "Arimo", Arial, sans-serif;
  }
  .canvas { position: relative; width: 1200px; height: 900px; }
  .card {
    position: absolute; left: 307px; width: 555px; height: 302px;
    box-shadow: 2px 3px 6px rgba(0,0,0,0.35);
    display: flex; flex-direction: column;
    color: var(--ink);
  }
  .card--lilac { top: 129px; background: var(--lilac); --band: var(--lilac-deep); --mark: var(--lilac-mark); --accent: var(--lilac-accent); }
  .card--pink { top: 461px; background: var(--pink); --band: var(--pink-deep); --mark: var(--pink-mark); --accent: var(--pink-accent); }
  .card__main { height: 236px; text-align: center; position: relative; }
  .card__title {
    position: absolute; top: 14px; left: 0; right: 0;
    font-size: 20px; font-weight: 700; letter-spacing: -0.3px;
  }
  .card__title em { font-size: 15px; font-style: italic; margin-left: 6px; }
  .card__services {
    position: absolute; top: 42px; left: 0; right: 0;
    font-size: 14.5px; font-weight: 700; color: var(--accent);
  }
  .brand {
    position: absolute; top: 72px; left: 50%; transform: translateX(-50%);
    width: 100px; height: 100px; border-radius: 50%;
    background: var(--mark);
    display: flex; align-items: center; justify-content: center;
  }
  .brand__name { font-size: 15px; font-weight: 700; color: var(--white); }
  .card__doctor {
    position: absolute; top: 170px; left: 0; right: 0;
    font-size: 19px; font-weight: 700; letter-spacing: -0.3px;
  }
  .card__cert {
    position: absolute; top: 196px; left: 0; right: 0;
    font-size: 12.5px; font-weight: 700; color: var(--accent);
  }
  .card__band {
    flex: 1; background: var(--band); color: var(--white);
    font-weight: 700; text-align: center;
    display: flex; flex-direction: column; justify-content: center; gap: 8px;
  }
  .card__address { font-size: 16.5px; }
  .card__contact { font-size: 15px; display: flex; justify-content: center; gap: 22px; }
</style>
</head>
<body>
<main class="canvas">
  <section class="card card--lilac">
    <div class="card__main">
      <p class="card__title">Women´s Health &amp; Wellness Specialist<em>by appoitment</em></p>
      <p class="card__services">OBSTETRICS - GYNECOLOGY - FAMILY PLANNING - MENOPAUSE</p>
      <div class="brand"><span class="brand__name">Willowbend</span></div>
      <p class="card__doctor">Corin Abbott - Wexley MD</p>
      <p class="card__cert">Board Certified</p>
    </div>
    <div class="card__band">
      <p class="card__address">418 Harbor Road, Millbrook NY 11090</p>
      <p class="card__contact"><span>PH: 555.014.2210/2211</span><span>FX: 555.014.2250</span><span>c-wexley@northmail.net</span></p>
    </div>
  </section>

  <section class="card card--pink">
    <div class="card__main">
      <p class="card__title">Women´s Health &amp; Wellness Specialist<em>by appoitment</em></p>
      <p class="card__services">OBSTETRICS - GYNECOLOGY - FAMILY PLANNING - MENOPAUSE</p>
      <div class="brand"><span class="brand__name">Willowbend</span></div>
      <p class="card__doctor">Corin Abbott - Wexley MD</p>
      <p class="card__cert">Board Certified</p>
    </div>
    <div class="card__band">
      <p class="card__address">207-40 Linden Parkway, Ashgrove New York 11499</p>
      <p class="card__contact"><span>PH: 555.018.3140</span><span>FX: 555.018.3141</span><span>c-wexley@northmail.net</span></p>
    </div>
  </section>
</main>
</body>
</html>
```